Tree Pruning Website

We need a website for a tree Arborist, pruning company called Hollow Ridge Groundcare. We look after all types of trees, knock down trees and prune trees. Our target market is from domestic clients to government clients and everything in between.

We would like to see the use of our main colours which are orange and green

We are not looking forward in seeing a template that we have seen before but a unique template. We have designed 5 templates ourselves and we wish for the design community to take our designs to the next level.

We have also designed a template for things that **we are not** looking for (Version 4)

To make it fair for everyone, we are also not giving out any participation payments as we have had. One winner will take all of the payment!!!

I Have attached a image of the designs and a image of a tree.

We are just looking at the PSD file been developed. We have our own team who can slice the image up into a HTML format.

Target Market(s)

Everyone who needs to cut down a tree

Industry/Entity Type

Government

Requirements
Must have
• Logo on front page
A List of our services
jQuery slider on page
Phone Number on every page

```html
<!DOCTYPE html>
<html lang="en">
<head>
<meta charset="utf-8">
<title>Hollow Ridge Groundcare</title>
<link href="https://fonts.googleapis.com/css2?family=Oswald:wght@400;500&family=Arimo:wght@400&display=swap" rel="stylesheet">
<style>
:root{
  --leaf:#8fc057;
  --leaf-light:#a3c964;
  --nav-green:#6cb33f;
  --nav-green-dark:#5a9e2f;
  --heading-green:#8bbd4a;
  --orange:#d4531c;
  --orange-dark:#b8451a;
  --bark:#5a3b18;
  --bark-dark:#4a2f12;
  --page:#f3f5ef;
  --text:#5a5a5a;
  --rule:#dcdfd6;
}
*{margin:0;padding:0;box-sizing:border-box}
html,body{width:1108px;height:1200px;overflow:hidden}
body{position:relative;background:var(--page);font-family:"Arimo",Arial,sans-serif;color:var(--text)}
.top-band{position:absolute;left:0;top:0;width:1108px;height:540px;background:linear-gradient(90deg,#93c25a 0%,var(--leaf-light) 20%,var(--leaf-light) 80%,#93c25a 100%)}
.site-frame{position:absolute;left:111px;top:37px;width:886px;height:522px;background:linear-gradient(#ffffff,#e4e4e2 110px,#f5f5f3 140px);box-shadow:0 2px 6px rgba(0,0,0,.18)}
.brand{position:absolute;left:132px;top:62px;display:flex;align-items:center;gap:10px}
.brand-dot{width:34px;height:34px;border-radius:50%;background:var(--nav-green)}
.brand-name{font-family:"Oswald",Arial,sans-serif;font-weight:500;font-size:26px;color:var(--nav-green);letter-spacing:.5px}
.phone{position:absolute;right:141px;top:76px;display:flex;align-items:center;gap:10px;font-family:"Oswald",Arial,sans-serif;font-size:22px;color:var(--orange)}
.main-nav{position:absolute;left:120px;top:150px;width:868px;height:46px;display:flex;background:linear-gradient(var(--nav-green),var(--nav-green-dark))}
.main-nav a{display:flex;align-items:center;justify-content:center;height:100%;color:#fff;text-decoration:none;font-family:"Oswald",Arial,sans-serif;font-size:14px;border-right:1px solid rgba(255,255,255,.12)}
.main-nav a.is-active{background:linear-gradient(var(--orange-dark),var(--bark))}
.hero-slider{position:absolute;left:120px;top:197px;width:868px;height:342px;background:linear-gradient(160deg,#7d8f6a 0%,#5f7440 35%,#d9d4c2 55%,#6b7d48 75%,#8e9aa8 100%)}
.slider-dots{position:absolute;left:885px;top:515px;display:flex;gap:8px}
.slider-dots span{width:11px;height:11px;border-radius:50%;background:var(--orange-dark)}
.sector{position:absolute;top:581px;width:212px;height:199px;border-radius:4px;overflow:hidden;background:#fff}
.sector h2{height:44px;background:var(--orange);color:#fff;font-family:"Oswald",Arial,sans-serif;font-weight:400;font-size:22px;text-align:center;line-height:44px}
.sector .photo{height:155px}
.services-box{position:absolute;left:111px;top:802px;width:222px;height:301px;background:#fff;border:1px solid var(--rule)}
.block-title{font-family:"Oswald",Arial,sans-serif;font-weight:400;font-size:19px;color:var(--heading-green)}
.services-box .block-title{padding:6px 8px;height:41px;border-bottom:1px solid var(--rule)}
.service-list{list-style:none;padding:10px 0 0 18px}
.service-list li{display:flex;align-items:center;gap:20px;height:27.7px;font-size:12px;color:#444}
.welcome{position:absolute;left:360px;top:806px;width:305px}
.welcome .block-title{height:38px;border-bottom:1px solid var(--rule);margin-bottom:12px}
.welcome p{font-size:10.8px;line-height:16.6px;text-align:justify;margin-bottom:17px;color:#666}
.projects{position:absolute;left:692px;top:806px;width:305px}
.projects .block-title{height:38px;border-bottom:1px solid var(--rule);margin-bottom:16px}
.project-grid{display:grid;grid-template-columns:148px 148px;gap:9px;column-gap:9px}
.project-grid div{height:113px}
.site-footer{position:absolute;left:0;top:1127px;width:1108px;height:73px;background:var(--bark)}
.copyright{position:absolute;left:111px;top:26px;font-size:11px;color:#f1eadf}
.social{position:absolute;left:851px;top:18px;display:flex;gap:8px}
.social span{width:32px;height:32px;border-radius:50%;background:#fff}
</style>
</head>
<body>
<div class="top-band"></div>
<div class="site-frame"></div>

<div class="brand"><span class="brand-dot"></span><span class="brand-name">Hollow Ridge Groundcare</span></div>

<div class="phone">
  <svg width="28" height="20" viewBox="0 0 28 20"><path d="M2 7c0-4 6-6 12-6s12 2 12 6v2h-6V6H8v3H2z" fill="#8bbd4a"/><rect x="5" y="9" width="18" height="10" rx="2" fill="#8bbd4a"/><circle cx="14" cy="14" r="3" fill="#fff"/></svg>
  <span>08 5550 0142</span>
</div>

<nav class="main-nav">
  <a class="is-active" style="width:124px">HOME</a>
  <a style="width:132px">ABOUT US</a>
  <a style="width:165px">OUR SERVICES</a>
  <a style="width:151px">GET A QUOTE</a>
  <a style="width:141px">OUR WORK</a>
  <a style="width:155px;border-right:0">CONTACT US</a>
</nav>

<div class="hero-slider" role="img" aria-label="Looking up into pale-barked gum tree branches against the sky"></div>
<div class="slider-dots"><span></span><span></span><span></span></div>

<div class="sector" style="left:111px"><h2>DOMESTIC</h2><div class="photo" role="img" aria-label="Sunlight streaming through forest trees" style="background:linear-gradient(135deg,#2f5a22,#a9c9a0 55%,#3d6a2a)"></div></div>
<div class="sector" style="left:335px"><h2>COMMERCIAL</h2><div class="photo" role="img" aria-label="Glass office building beside green foliage" style="background:linear-gradient(90deg,#2d5566,#6ea3b8 55%,#4c8a2e)"></div></div>
<div class="sector" style="left:560px"><h2>GOVERNMENT</h2><div class="photo" role="img" aria-label="Bright green tree standing in a park lawn" style="background:linear-gradient(#e4ecef,#9fd14a 45%,#5c8a30 80%,#7aa548)"></div></div>
<div class="sector" style="left:785px"><h2>NON - PROFIT</h2><div class="photo" role="img" aria-label="Lone spreading tree under a cloudy sky" style="background:linear-gradient(#8a9a7a,#3f6a2a 60%,#2f4a22)"></div></div>

<section class="services-box">
  <h3 class="block-title">OUR SERVICES</h3>
  <ul class="service-list">
    <li><svg width="12" height="10" viewBox="0 0 12 10"><path d="M1 5l3 3 7-7" fill="none" stroke="#d4531c" stroke-width="2"/></svg>Diacnosis</li>
    <li><svg width="12" height="10" viewBox="0 0 12 10"><path d="M1 5l3 3 7-7" fill="none" stroke="#d4531c" stroke-width="2"/></svg>Treatment</li>
    <li><svg width="12" height="10" viewBox="0 0 12 10"><path d="M1 5l3 3 7-7" fill="none" stroke="#d4531c" stroke-width="2"/></svg>Purning</li>
    <li><svg width="12" height="10" viewBox="0 0 12 10"><path d="M1 5l3 3 7-7" fill="none" stroke="#d4531c" stroke-width="2"/></svg>Tree Removal</li>
    <li><svg width="12" height="10" viewBox="0 0 12 10"><path d="M1 5l3 3 7-7" fill="none" stroke="#d4531c" stroke-width="2"/></svg>Stump Removal</li>
    <li><svg width="12" height="10" viewBox="0 0 12 10"><path d="M1 5l3 3 7-7" fill="none" stroke="#d4531c" stroke-width="2"/></svg>Cabling &amp; Bracing</li>
    <li><svg width="12" height="10" viewBox="0 0 12 10"><path d="M1 5l3 3 7-7" fill="none" stroke="#d4531c" stroke-width="2"/></svg>Arborist</li>
    <li><svg width="12" height="10" viewBox="0 0 12 10"><path d="M1 5l3 3 7-7" fill="none" stroke="#d4531c" stroke-width="2"/></svg>Consults</li>
    <li><svg width="12" height="10" viewBox="0 0 12 10"><path d="M1 5l3 3 7-7" fill="none" stroke="#d4531c" stroke-width="2"/></svg>Tree Protection</li>
  </ul>
</section>

<section class="welcome">
  <h3 class="block-title">WELCOME</h3>
  <p>ed ut perspiciatis unde omnis iste natus error sit voluptatem accusantium doloremque laudantium, totam rem aperiam, eaque ipsa quae ab illo inventore veritatis et quasi architecto beatae vitae dicta sunt explicabo.</p>
  <p>Nemo enim ipsam voluptatem quia voluptas sit aspernatur aut odit aut fugit, sed quia consequuntur magni dolores eos qui ratione voluptatem sequi nesciunt.</p>
  <p>Neque porro quisquam est, qui dolorem ipsum quia dolor sit amet, consectetur, adipisci velit, sed quia non numquam eius modi tempora incidunt ut labore et dolore magnam aliquam quaerat voluptatem. Ut enim ad minima veniam, quis nostrum exercitationem ullam corporis suscipit laboriosam, nisi ut aliquid ex ea commodi consequatur? Quis autem vel eum iure</p>
</section>

<section class="projects">
  <h3 class="block-title">LATEST PROJECTS</h3>
  <div class="project-grid">
    <div role="img" aria-label="Office facade behind leafy shrubs" style="background:linear-gradient(90deg,#3a6a86,#5ea12a 40%,#8cc63f)"></div>
    <div role="img" aria-label="Glass building with red-leaved garden plants" style="background:linear-gradient(#3f7fc4,#9ab5c8 45%,#8a4a2a 75%,#4a6a2a)"></div>
    <div role="img" aria-label="Curved office building with young trees" style="background:linear-gradient(#5a9ad8,#d9d9d2 50%,#5c8a36)"></div>
    <div role="img" aria-label="Modern glass building among trees" style="background:linear-gradient(#3a78c0,#8aa8c4 45%,#4a7a2e)"></div>
  </div>
</section>

<footer class="site-footer">
  <p class="copyright">© 2013 Hollow Ridge Groundcare. All Rights Reserved.</p>
  <div class="social" aria-label="Social links"><span></span><span></span><span></span><span></span></div>
</footer>
</body>
</html>
```